Brand new start up connecting advertisers to the gaming community needs a cool website design

The company is called Quenzly with the tagline "Gamers, Fans, and Brands". I connect the advertisers and their brands/services with sponsorship opportunities within the gaming community, which includes popular streamers, professional gamers and teams as well as venues that host popular events.

I need a website that's fun, eye-catching and playful but not at the expense of professionalism. I'm in the gaming space so some degree of playfulness within the site and context is desired.

As an example, I envision a plugin for the initial load screen where the letters of my logo (see uploaded files for visual) fall from the top of the screen upside down (hence the "quenzly") and bounce into place centered on the screen above the fold . Once that sequence concludes (a few seconds), it holds in place and then the letters turn into correct form to form the logo. After all that the tagline appears underneath. I think a 5 second total sequence of all this makes the most sense and it only loads when you initially visit.

I have other ideas but welcome yours. If you've worked in this esports/gaming environment before, I would love to hear your thoughts and suggestions. If you haven't, that's ok too.

Please keep in mind, I need to keep a professional tone throughout this project's design. Meridex 400 companies and the largest ad agencies in the world will be my clients. I need them to know that Quenzly is legit and credible not goofy and all "gamey"

Target Market(s)

it's two fold. The primary target will be adults 25-54 but a secondary target is streamers/gamers/video gaming community that is mostly male 12-34.

Industry/Entity Type

Advertising

Coding

Coded - Design and coding required

Number of Pages Required

4 page

Font styles to use
Sans Serif

Requirements
Must have
• A fun, playful website that is also professional.

I'm going to eventually drop in video examples of work I've done.

Cool backgrounds can either be developed or be from static pictures i own or use from large gaming tournaments showcasing the excitement around the experience.

Use whatever logo uploaded in the files that you think works best with your design
Nice to have
• Experiment with cool fonts as long as they are easy to read

Have fun with little "easter eggs" in the design such as things the visitors discovers when navigating the web page. Maybe when the cursor rolls over a letter in the logo, it reacts in a fun way such as inverting or expanding???

I'm open to anything fun as long as it doesn't dominate the experience. Playful should be limited to a few fun things but not be the epi-center of the experience.

If you want to explore other options or get better explanation on what this means, email me.
Should not have
• It shouldn't feel too business-like or static. I need a balance that leans professional with fun throughout that does NOT compromise the user's experience.

Do not play off of existing/traditional gaming clip art or proprietary trademarks like the velora symbol, Zentro logo, Moss Prowler monster, etc...

```html
<!DOCTYPE html>
<html lang="en">
<head>
<meta charset="utf-8">
<title>Quenzly — Gamers, Fans &amp; Brands</title>
<link href="https://fonts.googleapis.com/css2?family=Oswald:wght@300;500;700&family=Lato:wght@400;700&display=swap" rel="stylesheet">
<style>
:root{
  --red:#ff0000;
  --red-dark:#c00000;
  --black:#000000;
  --ink:#05070d;
  --field:#131313;
  --white:#ffffff;
  --muted:#d8d8d8;
}
*{box-sizing:border-box;margin:0;padding:0}
html,body{width:1200px;height:2343px;overflow:hidden;background:var(--black)}
body{position:relative;font-family:'Lato',sans-serif;color:var(--white)}
.abs{position:absolute}
.display{font-family:'Oswald',sans-serif;text-transform:uppercase}

/* Brand */
.brand{position:absolute;left:149px;line-height:1}
.brand-name{font-family:'Oswald',sans-serif;font-weight:500;font-size:38px;letter-spacing:7px;color:var(--red)}
.brand-tag{font-family:'Lato',sans-serif;font-weight:700;font-size:11px;letter-spacing:3px;color:var(--white);margin-top:4px}

/* Header */
.nav-slash{left:338px;top:32px}
.nav{left:350px;top:32px;width:700px;height:44px;background:var(--red)}
.nav-home{position:absolute;left:0;top:0;width:118px;height:44px;background:var(--red-dark);clip-path:polygon(6% 0,100% 0,88% 100%,0 100%)}
.nav a{position:absolute;top:13px;font-family:'Oswald',sans-serif;font-weight:500;font-size:13px;color:var(--white);text-decoration:none;text-transform:uppercase}

/* Hero */
.hero-photo{left:0;top:0;width:1200px;height:628px;
  background:radial-gradient(ellipse at 58% 40%,#1f5d8f 0%,#14305a 25%,#0b1330 50%,transparent 75%),
             radial-gradient(ellipse at 80% 30%,#a23a1a 0%,transparent 30%),
             radial-gradient(ellipse at 95% 50%,#2e4a6b 0%,transparent 40%),
             linear-gradient(180deg,#040813 0%,#070b18 80%,#000 100%)}
.hero-title{left:148px;top:238px}
.hero-title .l1{font-family:'Oswald',sans-serif;font-weight:300;font-size:44px;line-height:50px}
.hero-title .l2{font-family:'Oswald',sans-serif;font-weight:700;font-size:60px;line-height:70px;color:var(--red)}
.hero-title .l3{font-family:'Oswald',sans-serif;font-weight:700;font-size:82px;line-height:86px}
.dots{left:552px;top:582px}

/* Sections */
.section-title{font-family:'Oswald',sans-serif;font-weight:700;font-size:28px;text-transform:uppercase}
.section-title span{color:var(--red)}
.lead{font-size:14.5px;line-height:21px;color:var(--white)}
.ticks{list-style:none;margin-top:24px}
.ticks li{font-weight:700;font-size:17px;line-height:31.5px;padding-left:20px;position:relative}
.ticks li::before{content:"";position:absolute;left:1px;top:12px;border-left:6px solid var(--red);border-top:4px solid transparent;border-bottom:4px solid transparent}
.btn{position:absolute;width:128px;height:40px}
.btn svg{position:absolute;left:0;top:0}
.btn span{position:relative;display:block;line-height:40px;font-family:'Oswald',sans-serif;font-weight:500;font-size:14px;text-transform:uppercase}

.who-photo{left:0;top:663px;width:600px;height:332px;clip-path:polygon(0 0,523px 0,589px 332px,0 332px);
  background:radial-gradient(ellipse at 30% 75%,#7a1560 0%,transparent 45%),radial-gradient(ellipse at 75% 30%,#3a1030 0%,transparent 45%),linear-gradient(135deg,#1a1a22,#0c0c12)}
.who-text{left:657px;top:680px;width:400px}

.do-bg{left:0;top:995px;width:1200px;height:560px;
  background:radial-gradient(ellipse at 40% 75%,#5a2a10 0%,transparent 55%),radial-gradient(ellipse at 40% 5%,#2a1a45 0%,transparent 50%),linear-gradient(180deg,#080712 0%,#150c14 60%,#040406 100%)}
.do-photo{left:618px;top:1092px;width:582px;height:332px;clip-path:polygon(15px 0,582px 0,582px 332px,80px 332px);
  background:radial-gradient(ellipse at 50% 45%,#3a6a8a 0%,transparent 50%),radial-gradient(ellipse at 80% 70%,#8a5a3a 0%,transparent 45%),linear-gradient(135deg,#1c3f6a,#0d2036)}
.do-text{left:149px;top:1131px;width:420px}

/* Contact */
.contact-bg{left:0;top:1480px;width:1200px;height:808px;background:linear-gradient(180deg,transparent 0%,#03070c 30%,#020509 100%)}
.contact-head{left:0;top:1530px;width:1200px;text-align:center}
.contact-head p{font-size:15px;margin-top:10px}
.field{position:absolute;height:51px;border:1px solid var(--red-dark);background:var(--field);font-size:12px;padding:18px 28px;color:var(--muted)}
.field.message{height:182px}

/* Footer */
.contact-card{top:2042px;width:313px;height:56px}
.contact-card .txt{position:absolute;top:10px;line-height:1.2}
.contact-card small{font-size:12px;display:block}
.contact-card b{font-size:14px}
.socials{left:0;top:2172px;width:1200px;display:flex;justify-content:center;gap:38px}
.social{display:flex;align-items:center;gap:8px;font-weight:700;font-size:15px}
.social i{width:30px;height:30px;border-radius:50%;background:var(--white);display:block}
.copyright{left:0;top:2288px;width:1200px;height:55px;background:var(--red);text-align:center;line-height:55px;font-size:13px}
</style>
</head>
<body>

<!-- Hero -->
<div class="abs hero-photo" role="img" aria-label="Gamer at a glowing desk setup playing on a monitor, blue and orange room lighting"></div>

<header>
  <div class="brand" style="top:28px"><div class="brand-name">QUENZLY</div><div class="brand-tag">Gamers, Fans &amp; Brands</div></div>
  <svg class="abs nav-slash" width="20" height="44"><polygon points="10,0 16,0 6,44 0,44" fill="#fff"/></svg>
  <nav class="abs nav">
    <div class="nav-home"></div>
    <a href="#" style="left:50px">Home</a>
    <a href="#" style="left:148px">Who we are</a>
    <a href="#" style="left:282px">What we do</a>
    <a href="#" style="left:416px">Contact</a>
  </nav>
</header>

<div class="abs hero-title">
  <div class="l1">CONNECTING</div>
  <div class="l2">GAMERS, FANS</div>
  <div class="l3">&amp; BRANDS</div>
</div>
<svg class="abs dots" width="80" height="8">
  <polygon points="3,0 22,0 19,6 0,6" fill="#fff"/>
  <polygon points="30,0 49,0 46,6 27,6" fill="#ff0000"/>
  <polygon points="57,0 76,0 73,6 54,6" fill="#fff"/>
</svg>

<!-- Who we are -->
<div class="abs who-photo" role="img" aria-label="Gaming keyboard, headset and mouse on a neon-lit mouse pad"></div>
<svg class="abs" style="left:518px;top:663px" width="90" height="332"><polygon points="4,0 12,0 86,332 76,332" fill="#ff0000"/></svg>
<section class="abs who-text">
  <h2 class="section-title">Who we <span>are</span></h2>
  <p class="lead" style="margin-top:14px">Lorem ipsum dolor sit amet, consectetur adipiscing elit, sed do eiusmod tempor incididunt ut labore et dolore magna.</p>
  <ul class="ticks">
    <li>We create experiences</li>
    <li>We forge relationships</li>
    <li>We drive awareness</li>
    <li>We build communities</li>
  </ul>
</section>
<a class="btn" style="left:657px;top:941px"><svg width="128" height="40"><polygon points="0.5,0.5 126,0.5 114,39.5 0.5,39.5" fill="none" stroke="#ff0000"/></svg><span style="padding-left:23px">Read more</span></a>

<!-- What we do -->
<div class="abs do-bg" role="img" aria-label="Crowd at a live gaming event under stage lights"></div>
<div class="abs do-photo" role="img" aria-label="Hands on a backlit keyboard at a gaming desk"></div>
<svg class="abs" style="left:615px;top:1092px" width="90" height="332"><polygon points="3,0 12,0 86,332 76,332" fill="#ff0000"/></svg>
<section class="abs do-text">
  <h2 class="section-title">What we <span>do</span></h2>
  <p class="lead" style="margin-top:14px">Lorem ipsum dolor sit amet, consectetur adipiscing elit, sed do eiusmod tempor incididunt ut labore et dolore magna.</p>
  <ul class="ticks">
    <li>Sed ut perspiciatis unde omnis</li>
    <li>Sed ut perspiciatis unde omnis</li>
    <li>Sed ut perspiciatis unde omnis</li>
    <li>Sed ut perspiciatis unde omnis</li>
  </ul>
</section>
<a class="btn" style="left:150px;top:1390px"><svg width="128" height="40"><polygon points="0.5,0.5 126,0.5 114,39.5 0.5,39.5" fill="none" stroke="#ff0000"/></svg><span style="padding-left:24px">Read more</span></a>

<!-- Contact -->
<div class="abs contact-bg"></div>
<div class="abs contact-head">
  <h2 class="section-title">Contact <span>form</span></h2>
  <p>Get in touch with us</p>
</div>
<form>
  <div class="field" style="left:233px;top:1632px;width:236px">Name</div>
  <div class="field" style="left:481px;top:1632px;width:237px">Email</div>
  <div class="field" style="left:730px;top:1632px;width:237px">Subject</div>
  <div class="field message" style="left:233px;top:1700px;width:734px">Message</div>
</form>
<a class="btn" style="left:532px;top:1925px;width:142px"><svg width="142" height="40"><polygon points="0.5,0.5 141,0.5 128,39.5 13,39.5" fill="none" stroke="#ff0000"/></svg><span style="text-align:center">Send message</span></a>

<!-- Footer -->
<footer>
  <div class="brand" style="top:2040px"><div class="brand-name">QUENZLY</div><div class="brand-tag">Gamers, Fans &amp; Brands</div></div>

  <svg class="abs" style="left:385px;top:2042px" width="24" height="56"><polygon points="13,0 19,0 6,56 0,56" fill="#fff"/></svg>
  <div class="abs contact-card" style="left:397px">
    <svg class="abs" width="313" height="56"><polygon points="14,0 313,0 299,56 0,56" fill="#ff0000"/></svg>
    <svg class="abs" style="left:56px;top:14px" width="28" height="28" fill="none" stroke="#fff" stroke-width="1.5"><rect x="2" y="8" width="24" height="17"/><polyline points="2,8 14,17 26,8"/><circle cx="14" cy="10" r="4"/></svg>
    <div class="txt" style="left:97px"><small>Email us</small><b>hello@quenzlymail.net</b></div>
  </div>

  <svg class="abs" style="left:725px;top:2042px" width="24" height="56"><polygon points="13,0 19,0 6,56 0,56" fill="#fff"/></svg>
  <div class="abs contact-card" style="left:737px">
    <svg class="abs" width="313" height="56"><polygon points="14,0 313,0 299,56 0,56" fill="#ff0000"/></svg>
    <svg class="abs" style="left:77px;top:14px" width="28" height="28" fill="none" stroke="#fff" stroke-width="1.5"><path d="M5 3 L10 3 L12 9 L9 11 C11 16 13 18 18 20 L20 17 L26 19 L26 24 C26 26 24 27 22 27 C12 26 3 17 2 7 C2 5 3 3 5 3 Z"/></svg>
    <div class="txt" style="left:120px"><small>Call Now</small><b>(555)-014-2290</b></div>
  </div>

  <div class="abs socials">
    <span class="social"><i></i>Chirpa</span>
    <span class="social"><i></i>Snapgrid</span>
    <span class="social"><i></i>Linkport</span>
  </div>

  <div class="abs copyright">Copyright, © 2020 All rights reserved</div>
</footer>

</body>
</html>
```